Web Design - Fitness for Middle Age Women

I need a web design for a start-up personal training company in Los Alamitos, CA called 'Maple Fitness & Health.' I would like to cater personal training services to middle-age mothers (30-50 years of age) who have kids and who would also want their children to receive services. The attached file is the logo of the company. Keep in mind the theme colors are white and blue and black, but make the background/pictures appealing to middle-age mothers. I want the flow of the website to be easy to use. The final design should present the company as a professional personal training service.

I realize this is a low budget project for designers but this is a budget I have to offer at the moment and if I take your design I will make sure to come back to improve the site when I'm able to gain more capital. I am looking for a full website built (using wordpress) with the following tabs (About / FAQ / Services / Clients / Location / Contact Us...and social media links to Twitter / Instagram / Facebook)
Updates

I am looking over the current designs and narrowing down the decision. A decision will be made in the next 24-48 hours.

Target Market(s)

Middle-age mothers (30-55 years of age) who have children, an established career (or husband who is the bread-winner of the house) and has forgotten to take care of themselves and their body for years. I want them to realize lifestyle change is a choice, and it is a choice they need to make for themselves and their family to be a proper pattern for their children.

Industry/Entity Type

Fitness

Requirements
Must have
• The logo I have attached.

```html
<!DOCTYPE html>
<html lang="en">
<head>
<meta charset="utf-8">
<title>Maple Fitness &amp; Health</title>
<link href="https://fonts.googleapis.com/css2?family=Cinzel:wght@400;600&family=Questrial&family=Arimo&display=swap" rel="stylesheet">
<style>
:root{
  --navy:#17175c;
  --navy-deep:#0f0f4a;
  --panel:#5b5d6e;
  --dark:#2b2b2e;
  --ink:#333;
  --muted:#555;
  --white:#fff;
  --rule:#bbb;
  --black:#1a1a1a;
}
*{margin:0;padding:0;box-sizing:border-box}
html,body{width:1009px;height:1200px;overflow:hidden;background:var(--white)}
body{position:relative;font-family:"Questrial",sans-serif;color:var(--ink)}
.abs{position:absolute}
.backdrop-left{left:0;top:0;width:189px;height:756px;background:
  linear-gradient(180deg,rgba(255,255,255,0) 55%,#fff 100%),
  linear-gradient(90deg,#b59a52 0%,#c7ae6a 4%,#5f86b4 12%,#3f6d9f 40%,#9db3c9 70%,#e8ecef 100%)}
.backdrop-right{left:819px;top:0;width:190px;height:756px;background:
  linear-gradient(180deg,rgba(255,255,255,0) 50%,#fff 100%),
  linear-gradient(180deg,#6e7378 0%,#c9ced2 20%,#eef0f2 45%,#e3e6e8 70%,#fff 100%)}
.page{left:189px;top:0;width:630px;height:1200px;background:var(--white)}
.brand{display:flex;align-items:center;gap:8px}
.brand-mark{width:50px;height:50px;border-radius:50%;background:var(--navy)}
.brand-name{font-family:"Cinzel",serif;font-size:13px;line-height:14px;color:var(--black)}
.header-brand{left:206px;top:12px}
.social-top{left:742px;top:16px;display:flex;gap:5px}
.social-top span{width:9px;height:9px;background:#222;border-radius:2px}
.nav{left:437px;top:40px;display:flex;gap:17px;font-family:"Cinzel",serif;font-size:10.5px;color:var(--black);letter-spacing:.3px}
.hero{left:196px;top:73px;width:615px;height:277px;background:
  radial-gradient(ellipse 90px 70px at 22% 30%,rgba(70,130,190,.9),rgba(70,130,190,0)),
  radial-gradient(ellipse 90px 60px at 53% 80%,rgba(220,80,140,.85),rgba(220,80,140,0)),
  radial-gradient(ellipse 120px 140px at 42% 55%,rgba(30,30,36,.85),rgba(30,30,36,0)),
  radial-gradient(ellipse 110px 150px at 75% 60%,rgba(30,30,36,.85),rgba(30,30,36,0)),
  linear-gradient(180deg,#e7e8ea 0%,#d6d8dc 55%,#9a6e55 85%,#7d5642 100%)}
.hero-band{left:196px;top:350px;width:615px;height:9px;background:var(--navy-deep)}
.hero-caption{left:334px;top:296px;width:327px;height:62px;background:var(--navy-deep);text-align:center;color:var(--white);padding-top:14px}
.hero-caption h1{font-family:"Cinzel",serif;font-weight:400;font-size:16px;letter-spacing:.6px}
.hero-caption p{font-size:8px;line-height:10.5px;color:#b8b8d0;padding:1px 26px 0}
.program-photo{top:360px;width:97px;height:102px}
.photo-family{left:196px;background:linear-gradient(135deg,#6f8fbf 0%,#c8d2e2 35%,#ead7c9 60%,#f4f4f6 80%,#3e4f78 100%)}
.photo-solo{left:504px;background:linear-gradient(135deg,#3a3a3e 0%,#6b6e74 30%,#d9c2a4 50%,#2a2a2e 75%,#1d1d20 100%)}
.program-panel{top:360px;height:102px;background:var(--panel);color:var(--white);padding:26px 15px 0 16px}
.panel-family{left:293px;width:211px}
.panel-solo{left:601px;width:210px}
.program-panel h2{font-family:"Cinzel",serif;font-weight:400;font-size:15px;letter-spacing:.4px;margin-bottom:4px}
.program-panel p{font-size:8.2px;line-height:10.8px}
.feature{width:242px}
.feature h3{font-family:"Cinzel",serif;font-weight:600;font-size:16px;line-height:18px;color:var(--navy);letter-spacing:.4px;margin-bottom:7px}
.feature p{font-size:8.4px;line-height:10.8px;text-transform:uppercase;color:var(--muted);letter-spacing:.15px;padding-right:6px}
.dark-band{left:196px;top:750px;width:615px;height:325px;background:var(--dark)}
.coach{width:180px;text-align:center;color:var(--white)}
.coach-photo{width:152px;height:152px;border-radius:50%;margin:0 auto 22px}
.coach h4{font-family:"Cinzel",serif;font-weight:600;font-size:11.5px;line-height:14px;letter-spacing:.4px;margin-bottom:12px;color:#f2f2f2}
.coach p{font-size:8.4px;line-height:10.6px;color:#e6e6e6;width:156px;margin:0 auto}
.footer-brand{left:198px;top:1096px}
.footer-nav{left:434px;top:1113px;font-family:"Arimo",sans-serif;font-size:7.8px;color:var(--black)}
.footer-nav span{color:var(--black)}
.footer-contact{left:670px;top:1101px;width:139px;text-align:right;font-family:"Arimo",sans-serif;font-size:6.8px;line-height:8px;color:var(--black)}
.phone{display:flex;justify-content:flex-end;align-items:center;gap:5px;font-size:11.5px;margin-top:4px}
.footer-rule{left:198px;top:1161px;width:611px;height:1px;background:var(--rule)}
.copyright{left:198px;top:1173px;font-family:"Arimo",sans-serif;font-size:7.3px;color:var(--black)}
.social-foot{left:702px;top:1170px;display:flex;gap:5px}
.social-foot span{width:18px;height:18px;border-radius:50%;background:#444}
</style>
</head>
<body>
<div class="abs backdrop-left" role="img" aria-label="Gym interior with blue walls, wooden pillars and rows of exercise bikes"></div>
<div class="abs backdrop-right" role="img" aria-label="Bright white gym room with treadmill and large windows"></div>
<div class="abs page"></div>

<header>
  <div class="abs brand header-brand">
    <span class="brand-mark"></span>
    <span class="brand-name">Maple<br>Fitness &amp; Health</span>
  </div>
  <div class="abs social-top" aria-label="Social links"><span></span><span></span><span></span><span></span></div>
  <nav class="abs nav"><span>About</span><span>FAQ</span><span>Services</span><span>Clients</span><span>Location</span><span>Contact Us</span></nav>
</header>

<section>
  <div class="abs hero" role="img" aria-label="Mothers and daughters exercising together with fitness balls and resistance bands"></div>
  <div class="abs hero-band"></div>
  <div class="abs hero-caption">
    <h1>LIFESTYLE CHANGE IS A CHOICE!</h1>
    <p>A choice you need to make for yourselves and your family to be a proper pattern for your children.</p>
  </div>
</section>

<section>
  <div class="abs program-photo photo-family" role="img" aria-label="Women in a group workout class"></div>
  <div class="abs program-panel panel-family">
    <h2>FAMILY PROGRAM</h2>
    <p>Lorem ipsum dolor sit amet, consectetur adipiscing elit, sed do eiusmod tempor incididunt ut labore et dolore magna.</p>
  </div>
  <div class="abs program-photo photo-solo" role="img" aria-label="Woman training on a gym machine"></div>
  <div class="abs program-panel panel-solo">
    <h2>SOLO PROGRAM</h2>
    <p>Lorem ipsum dolor sit amet, consectetur adipiscing elit, sed do eiusmod tempor incididunt ut labore et dolore magna liqua.</p>
  </div>
</section>

<section>
  <div class="abs feature" style="left:228px;top:516px">
    <h3>WEIGHT LOSS GETTING<br>STARTED</h3>
    <p>Praesent vestibulum aenean nonummy hendrerit mauris. Cum sociis natoque penatibus et mgnis dis parturient montes ascetur ridiculus mus. Nulla dui.</p>
  </div>
  <div class="abs feature" style="left:542px;top:516px">
    <h3>NUTRITION &amp;<br>SUPPLEMENTS</h3>
    <p>Praesent vestibulum aenean nonummy hendrerit mauris. Cum sociis natoque penatibus et mgnis dis parturient montes ascetur ridiculus mus. Nulla dui.</p>
  </div>
  <div class="abs feature" style="left:228px;top:632px">
    <h3>PROGRAM FOR<br>BEGINNERS</h3>
    <p>Praesent vestibulum aenean nonummy hendrerit mauris. Cum sociis natoque penatibus et mgnis dis parturient montes ascetur ridiculus mus. Nulla dui.</p>
  </div>
  <div class="abs feature" style="left:542px;top:632px">
    <h3>USEFUL TIPS<br>&amp; ADVICE</h3>
    <p>Praesent vestibulum aenean nonummy hendrerit mauris. Cum sociis natoque penatibus et mgnis dis parturient montes ascetur ridiculus mus. Nulla dui.</p>
  </div>
</section>

<section>
  <div class="abs dark-band"></div>
  <div class="abs coach" style="left:210px;top:786px">
    <div class="coach-photo" role="img" aria-label="Trainer lifting a dumbbell" style="background:radial-gradient(circle at 55% 40%,#b9c1c8 0%,#7d8a94 45%,#3e4850 100%)"></div>
    <h4>DOLORE CLASRTYA SIASE<br>KERANE NASER</h4>
    <p>Viloase magna onumsan erahaseres adelesas maltaliqueo.</p>
  </div>
  <div class="abs coach" style="left:414px;top:786px">
    <div class="coach-photo" role="img" aria-label="Smiling trainer with a towel in the gym" style="background:radial-gradient(circle at 45% 40%,#ecdccd 0%,#d9d3cd 50%,#a9a7a6 100%)"></div>
    <h4>PENERTS EXERCIBO VERO<br>NOERTY LERASE</h4>
    <p>Viloase magna onumsan erahaseres adelesas maltaliqueo.</p>
  </div>
  <div class="abs coach" style="left:621px;top:786px">
    <div class="coach-photo" role="img" aria-label="Trainer holding dumbbells" style="background:radial-gradient(circle at 50% 45%,#7a6050 0%,#3a2e29 50%,#1c1c1f 100%)"></div>
    <h4>DOLORE CLASRTYA SIASE<br>KERANE NASER</h4>
    <p>Viloase magna onumsan erahaseres adelesas maltaliqueo.</p>
  </div>
</section>

<footer>
  <div class="abs brand footer-brand">
    <span class="brand-mark"></span>
    <span class="brand-name">Maple<br>Fitness &amp; Health</span>
  </div>
  <div class="abs footer-nav"><span>About</span> &nbsp;|&nbsp; <span>FAQ</span> &nbsp;|&nbsp; <span>Services</span> &nbsp;|&nbsp; <span>Clients</span> &nbsp;|&nbsp; <span>Location</span> &nbsp;|&nbsp; <span>Contact Us</span></div>
  <div class="abs footer-contact">
    14 Harbor Lane Studio<br>Los Alamitos, CA 90720
    <div class="phone">
      <svg width="13" height="13" viewBox="0 0 13 13" aria-hidden="true"><circle cx="6.5" cy="6.5" r="5.8" fill="none" stroke="#222" stroke-width="1"/><path d="M4.3 3.6c.4-.3.8-.2 1 .2l.5 1c.1.3 0 .6-.2.8l-.3.3c.3.7.8 1.2 1.5 1.5l.3-.3c.2-.2.5-.3.8-.2l1 .5c.4.2.5.6.2 1-.5.6-1.2.8-1.9.5C5.7 8.5 4.5 7.3 3.9 5.8c-.3-.7-.1-1.5.4-2.2z" fill="#222"/></svg>
      555-0142-880
    </div>
  </div>
  <div class="abs footer-rule"></div>
  <div class="abs copyright">Copyright © 2014 | Privacy Policy</div>
  <div class="abs social-foot" aria-label="Social links"><span></span><span></span><span></span><span></span><span></span></div>
</footer>
</body>
</html>
```